crime story needs easy cover/ Krimi braucht Cover
Zielgruppe
Krimiautorin, Leser
Aufgabenstellung
Titel: 'Lotte. Grabreden, Gifte & Co.', Autorin: Henrike Brückner,
Layout: siehe Skribble, unten sollten von links nach rechts abgebildet sein: Pudel, Perückenkopf mit Perücke, Mia mit Noten um den Kopf, Bonsai und Luftballon. Das kann gerne Comic-artig sein, aber kein Manga-Stil und bitte nicht nur Umrisse, falls möglich. Mia hat kurze rote Locken, trägt ein Ringelshirt und Jeans. SIe ist kein Girlie. Cover-Farbe: knallig. Auf der Rückseite muss ich noch einen Klappentext einfügen. Und es fehlt noch ein ISBN, das müsste nachträglich noch eingefügt werden.
Title of book: 'Lotte. Grabreden, Gifte & Co.'; Author: Henrike Brückner
Layout: see scribble, from left to right: a poodle, a wig holder and a wig, Mia with music notes, a Bonsai and a ballon. Mia has curly red hair, is wearing a shirt in stripes and a jeans, she is not a 'girlie'. And please complete figures, not only 'frames(?). Can be a comic, but no manga. Colour: gaudy (?). Blurb for the back will follow, also ISBN.

```html
<!DOCTYPE html>
<html lang="de">
<head>
<meta charset="utf-8">
<title>Lotte – Grabreden, Gifte &amp; Co</title>
<link rel="stylesheet" href="https://fonts.googleapis.com/css2?family=Josefin+Sans:wght@700&family=Quicksand:wght@700&family=Merriweather:wght@400&display=swap">
<style>
  :root {
    --page: #ffffff;
    --cover: #833888;
    --cover-light: #9a52a0;
    --cover-soft: #b57bb9;
    --ink: #ffffff;
  }
  html, body {
    margin: 0;
    width: 1200px;
    height: 1200px;
    overflow: hidden;
    background: var(--page);
  }
  .book-cover {
    position: absolute;
    left: 203px;
    top: 37px;
    width: 794px;
    height: 1123px;
    background: var(--cover);
    color: var(--ink);
  }
  .volume-tag {
    position: absolute;
    right: 29px;
    top: 0;
    width: 149px;
    height: 68px;
    background: var(--ink);
    color: var(--cover);
    font-family: "Merriweather", serif;
    font-size: 27px;
    line-height: 68px;
    text-align: center;
    letter-spacing: 0.5px;
  }
  .title {
    position: absolute;
    left: 0;
    right: 0;
    top: 198px;
    margin: 0;
    text-align: center;
    font-family: "Josefin Sans", sans-serif;
    font-weight: 700;
    font-size: 232px;
    line-height: 1;
    letter-spacing: 4px;
  }
  .subtitle {
    position: absolute;
    left: 0;
    right: 0;
    top: 472px;
    margin: 0;
    text-align: center;
    font-family: "Quicksand", sans-serif;
    font-weight: 700;
    font-size: 38px;
    line-height: 1.2;
  }
  .genre {
    position: absolute;
    left: 0;
    right: 0;
    top: 562px;
    margin: 0;
    text-align: center;
    font-family: "Merriweather", serif;
    font-size: 23px;
  }
  .scene-art {
    position: absolute;
    left: 197px;
    top: 610px;
    width: 433px;
    height: 320px;
  }
  .author {
    position: absolute;
    left: 0;
    right: 0;
    top: 1020px;
    margin: 0;
    text-align: center;
    font-family: "Merriweather", serif;
    font-weight: 400;
    font-size: 50px;
    letter-spacing: 0.5px;
  }
</style>
</head>
<body>
  <main class="book-cover">
    <div class="volume-tag">BAND I</div>
    <h1 class="title">LOTTE</h1>
    <p class="subtitle">Grabreden, Gifte &amp; Co</p>
    <p class="genre">Kriminalroman</p>
    <svg class="scene-art" viewBox="0 0 433 320" role="img" aria-label="Comic-Illustration: Pudel, Perückenkopf mit blonder Perücke, rothaarige Frau im Ringelshirt mit Musiknoten, Bonsai und blauer Luftballon">
      <defs>
        <linearGradient id="sceneTone" x1="0" y1="0" x2="0" y2="1">
          <stop offset="0" stop-color="var(--cover-light)" stop-opacity="0.35"/>
          <stop offset="1" stop-color="var(--cover-soft)" stop-opacity="0.55"/>
        </linearGradient>
      </defs>
      <rect x="0" y="0" width="433" height="320" rx="18" fill="url(#sceneTone)"/>
    </svg>
    <p class="author">Henrike Brückner</p>
  </main>
</body>
</html>
```